Race car follow-up website needs web design

We are currently finalising a website which allows amateur and professional owners of race cars to track the running time of the car and all installed parts (drive shafts, gearbox etc.). The site is working for a technical point of view, but needs a nice design applied to it.

The website is made with Bootstrap 3.x and does not need a mobile skin. We target desktop and tablet users. This means that the delivered work should be easy to incorporate in the Bootstrap site that currently exists, from a technical point of view.

In attachment you can find all the screens that need skinning. If you think some stuff can be done better from a usability or design point of view (size of tables, placement of buttons etc.), do not hesitate to make a suggestion. We are open to positive criticism, and the current "base" design is not carved in stone. The colors currently used are basic Bootstrap so that can change too. There are no limits whatsoever, as long as the result looks good.

We have a big amount of racing/racecar/mechanic/pitbox related photo material that can be used, so do not hesitate to ask for material if needed.

The start page should be something along the lines of these sites:

https://plumvex.me/
http://quorvane.io/
https://teldrova.com/
http://www.mivostrel.com/

Or in words: a top navigation bar (as seen in the screenshots). A full-width image relevant to the content (racing related) with some text in overlay (A sort of slogan along the lines of "Let us track your parts" or "Parts tracking for you race or trackday car" ). Under that image there should then be a very high-level overview of what the website can be used for (In a few steps, with graphics/photos, schematics, showing driving the car, data transfer, management in the site.). This so the potential user can quickly see if it is of any interest to him/her.

Basically:

Drive --- Download data -- Get Alerted

each step should contain an "icon" representing what it is about, and a few lines of text explaining what is meant.

On that page (in the image part, or below the explanation) there should be 2 links (buttons). One leads to the pricing page, one to the registration page.

Of course this first page cannot be finalised until we give the complete details of the content, so please provide a high-level design and the person I work with will receive the detailed specs (the text for the different steps etc).

The other screens are (we think) self-explanatory. Please look at them in chronological order (they are prefixed 00 to 19)

There are screenshots of the manual. This page will also need to be styled (to match the rest of the site and to make the layout a bit more sexy). We will of course provide the original html file to this once the content needs to be finalised.

Besides the website, a mail template is required too. The site sends mails for:
- registration confirmation
- lost password
- alerts related to the car parts or the data files.

These mails should also have a professional looking skin (right now they are plain text)

Just to make things clear, if you think the base design we made is "crap", please suggest improvements (for instance, menu placement in the bottom, positioning of certain elements, tables that might be better off somewhere else, the car details on top that take too much screen real-estate etc. etc.). This site has been built by developers, not by designers. The only condition is that it should be technically possible in a reasonable amount of time using Bootstrap 3.x

Please provide the resources in such a way that a developer with web skills can directly implement them. So any slicing of graphics should be done by the designer. If you only provide us a good looking psd file we won't be able to do anything with that, unfortunately.

If you, as a designer, have a passion for sports cars, race cars, trackdays and/or GT car racing, this is of course a plus. The collaboration will be a lot easier if we speak the same "language".

Please provide at least a design of
- the start page
- the "car details" page
- one of the list modals
- one of the form modals

so we can at least know how the rest of the pages will look

The name is Pitlane Ledger.

Some pictures that can be used:

https://www.snapvelo.com/photos/58310472@K04/20581937466/
https://www.snapvelo.com/photos/58310472@K04/4815209367/
https://www.snapvelo.com/photos/58310472@K04/4812766058/
https://www.snapvelo.com/photos/58310472@K04/4801533729/
https://www.snapvelo.com/photos/58310472@K04/4763921850/
https://www.snapvelo.com/photos/58310472@K04/4706418592/
https://www.snapvelo.com/photos/58310472@K04/4594071683/
https://www.snapvelo.com/photos/58310472@K04/4361829074/
https://www.snapvelo.com/photos/58310472@K04/3958316247/
https://www.snapvelo.com/photos/58310472@K04/3927140568/
https://www.snapvelo.com/photos/58310472@K04/3915762839/
https://www.snapvelo.com/photos/58310472@K04/3915764901/
https://www.snapvelo.com/photos/58310472@K04/3890417352/
https://www.snapvelo.com/photos/58310472@K04/3885093716/
https://www.snapvelo.com/photos/58310472@K04/3885097284/
https://www.snapvelo.com/photos/58310472@K04/2081359647/
https://www.snapvelo.com/photos/58310472@K04/2398640513/
https://www.snapvelo.com/photos/58310472@K04/2486075129/
https://www.snapvelo.com/photos/58310472@K04/2323149876/
https://www.snapvelo.com/photos/58310472@K04/2323154902/

Basically you take whatever you want from this guy’s photo stream:
https://www.snapvelo.com/photos/58310472@K04/

I know him personally so there should be no copyright issues.

Most users of the site will run so called "GT" cars (Valdorni, Castruzzo etc.), so please refrain from using (or referencing) open wheelers, F1, LMP etc.

There is a logo contest too: http://gigs.pixelbazaar.com/gig.aspx?id=837461

I just updated the brief with some more info and images you can use.

I have updated the brief. This is added: for the first screen, the schematics are explained in a bit more detail: Basically: Drive ---> Download data --> Get Alerted each step should contain an "icon" representing what it is about, and a few lines of text explaining what is meant.

Dear designers, As we have received numerous remarks about our contest from you and your colleagues we have contacted PixelBazaar to solve the situation. This contest will be split into two different contests. One logo design contest for $400 and one website design contest for the $1480. Everyone who has submitted logos can of course participate with those logos in the logo design contest (there are a few that we like, which have been submitted). We are very sorry for the inconvenience we might have caused, and if you want to redraw your designs already submitted because of this we will fully understand this, but we hope this decision will make things clearer for everyone participating. As soon as matters are changed we will send you all a new message with the updated information. Thanks for your understanding. Morlek BVBA

The logo contest has been created: http://gigs.pixelbazaar.com/gig.aspx?id=837461

Reason: Because of the split in webdesign / logo the deadline has been extended so non-logo webdesigners can participate too. Logo project: http://gigs.pixelbazaar.com/gig.aspx?id=837461

The pricing page has been added in the screenshots section

Trackday enthousiasts, race car owners, race teams.

• No video
No huge "footer" with a lot of links to navigate the site, since there will be very litte content.
No references to non-GT type cars (so no F1, no Series Quelmont, no LMP1/LMP2) or street cars.

```html
<!DOCTYPE html>
<html lang="en">
<head>
<meta charset="utf-8">
<title>Pitlane Ledger – Car user permissions</title>
<link rel="stylesheet" href="https://fonts.googleapis.com/css2?family=Open+Sans:ital,wght@0,400;0,600;1,700&family=Russo+One&display=swap">
<style>
  :root {
    --black: #000000;
    --ink: #111111;
    --lime: #b7c35a;
    --lime-bright: #c8d46a;
    --lime-dark: #4b5320;
    --olive: #6f7a2a;
    --white: #ffffff;
    --grey-band: #8c8c8c;
    --grey-light: #c9c9c9;
    --grey-dark: #1d1d1d;
    --footer-text: #3e3e3e;
    --photo-dark: #1a1c1b;
    --photo-mid: #3a3d3b;
  }
  * { box-sizing: border-box; margin: 0; padding: 0; }
  html, body { width: 1200px; height: 972px; overflow: hidden; background: var(--black); }
  body { position: relative; font-family: "Open Sans", Arial, sans-serif; }

  .site-header { position: absolute; left: 0; top: 0; width: 1200px; height: 87px; background: var(--black); overflow: hidden; }
  .header-backdrop-name {
    position: absolute; left: 210px; top: 8px;
    font-family: "Russo One", Arial, sans-serif; font-size: 66px; letter-spacing: 2px;
    color: #262626; white-space: nowrap; text-transform: uppercase;
  }
  .brand {
    position: absolute; left: 158px; top: 26px;
    font-family: "Russo One", Arial, sans-serif; font-size: 26px; color: var(--white);
    text-transform: uppercase; letter-spacing: 1px;
  }
  .main-nav { position: absolute; left: 745px; top: 56px; display: flex; gap: 14px; }
  .main-nav a { color: var(--white); text-decoration: none; font-size: 20px; }
  .main-nav a.is-active { color: var(--lime-bright); }

  .header-rule { position: absolute; left: 0; top: 87px; width: 1200px; height: 8px; background: linear-gradient(180deg, #b5b5b5, #6a6a6a); }

  .hero-photo {
    position: absolute; left: 0; top: 95px; width: 1200px; height: 805px;
    background: radial-gradient(ellipse at 70% 45%, var(--photo-mid) 0%, var(--photo-dark) 70%);
  }

  .modal {
    position: absolute; left: 243px; top: 166px; width: 714px; height: 353px;
    border: 3px solid var(--lime); border-radius: 8px;
    background: linear-gradient(180deg, var(--grey-light) 0%, #a9a9a9 40%, #3a3a3a 78%, var(--grey-dark) 100%);
  }
  .modal-title {
    position: absolute; left: 44px; top: 9px; width: 598px; height: 28px;
    background: var(--lime); text-align: center;
    font-family: "Russo One", Arial, sans-serif; font-style: italic; font-size: 22px;
    letter-spacing: 3px; line-height: 28px; color: var(--ink); text-transform: uppercase;
  }
  .modal-close {
    position: absolute; left: 666px; top: 2px; width: 42px; height: 30px;
    background: var(--lime); border: 3px solid var(--lime-dark); border-radius: 3px;
    font-weight: 700; font-size: 16px; line-height: 22px; text-align: center; color: var(--ink);
  }
  .field-label { position: absolute; top: 96px; font-size: 19px; color: var(--ink); }
  .label-email { left: 76px; }
  .label-modify { left: 340px; }
  .label-remove { left: 558px; }

  .email-input {
    position: absolute; left: 36px; top: 135px; width: 262px; height: 30px;
    background: var(--white); border: 4px solid var(--lime-dark); border-radius: 10px;
  }
  .modify-check {
    position: absolute; left: 396px; top: 134px; width: 41px; height: 30px;
    background: var(--white); border: 4px solid var(--lime-dark); border-radius: 5px;
  }
  .remove-button {
    position: absolute; left: 576px; top: 134px; width: 40px; height: 30px;
    background: linear-gradient(180deg, #c6d066, #8d9838); border: 4px solid var(--lime-dark); border-radius: 4px;
    font-weight: 700; font-size: 15px; line-height: 21px; text-align: center; color: var(--ink);
  }
  .btn {
    position: absolute; height: 34px;
    background: linear-gradient(180deg, #d4dd78 0%, var(--lime) 45%, var(--olive) 100%);
    border: 4px solid #3c4218; border-radius: 3px;
    font-style: italic; font-weight: 700; font-size: 15px; line-height: 26px;
    text-align: center; color: var(--ink);
  }
  .btn-add-user { left: 36px; top: 179px; width: 132px; }
  .btn-save { left: 349px; top: 269px; width: 134px; }
  .btn-cancel { left: 528px; top: 269px; width: 134px; color: var(--white); }

  .site-footer-rule { position: absolute; left: 0; top: 900px; width: 1200px; height: 8px; background: linear-gradient(180deg, #9a9a9a, #5a5a5a); }
  .site-footer {
    position: absolute; left: 0; top: 908px; width: 1200px; height: 64px; background: var(--black);
    text-align: center; font-size: 16px; line-height: 68px; color: var(--footer-text);
  }
</style>
</head>
<body>
  <header class="site-header">
    <div class="header-backdrop-name" aria-hidden="true">Pitlane Ledger</div>
    <div class="brand">Pitlane Ledger</div>
    <nav class="main-nav">
      <a href="#">Home</a>
      <a href="#">Register</a>
      <a href="#" class="is-active">My cars</a>
      <a href="#">Contct us</a>
    </nav>
  </header>
  <div class="header-rule"></div>

  <div class="hero-photo" role="img" aria-label="Dark photograph of the rear of a GT race car on a pit lane"></div>

  <section class="modal" aria-labelledby="modal-title">
    <h1 class="modal-title" id="modal-title">Car user permissions</h1>
    <div class="modal-close">x</div>
    <span class="field-label label-email">E-mail</span>
    <span class="field-label label-modify">Can modify parts</span>
    <span class="field-label label-remove">Remove</span>
    <div class="email-input"></div>
    <div class="modify-check"></div>
    <div class="remove-button">x</div>
    <div class="btn btn-add-user">Add user</div>
    <div class="btn btn-save">Save</div>
    <div class="btn btn-cancel">Cancel</div>
  </section>

  <div class="site-footer-rule"></div>
  <footer class="site-footer">Copyright 2014 Pitlane Ledger | All rights reserved.</footer>
</body>
</html>
```